Webdesign für Training & Coaching rund um Geburt
Zielgruppe
Wallbrecht - Training & Coaching Rund um Geburt
Ich biete Kommunikationstrainings für Geburtshilfeteams an - Zielgruppe sind also Hebammen und ÄrztInnen. Es geht darum, dass sie mit den Gebärenden bewusster und besser kommunizieren, so dass Geburt stressfreier und störungsfreier ablaufen kann. Zum Nutzen der Frauen und Kinder und auch zum Nutzen der GeburtshelferInnen - indem sie einen stressfreieren Alltag haben.
Die Hauptzielgruppe sind Ärzte, Hebammen und vor allem auch Verwaltungsdirektoren von Kliniken, die Geld für die Fortbildung locker machen müssen. Deshalb bitte keine verspielten, esoterischen oder all zu weiblichen Entwürfe - eine klare Sache sollte es sein ,-))
Viel Spaß, ich bin gespannt!
Aufgabenstellung
siehe Briefing Datei

```html
<!DOCTYPE html>
<html lang="de">
<head>
<meta charset="utf-8">
<title>Wallbrecht – Training &amp; Coaching rund um Geburt</title>
<link href="https://fonts.googleapis.com/css2?family=Montserrat:wght@300;400;500;600&display=swap" rel="stylesheet">
<style>
:root{
  --blue:#1f68a4;
  --blue-dark:#1b5e96;
  --sky:#2aa3dc;
  --text:#4a4a4a;
  --line:#c9c9c9;
  --field:#f4f4f4;
  --white:#ffffff;
}
*{box-sizing:border-box;margin:0;padding:0}
html,body{width:1200px;height:3983px;overflow:hidden;background:var(--white)}
body{position:relative;font-family:"Montserrat",Arial,sans-serif;color:var(--text)}
.abs{position:absolute}
.brand-name{font-weight:400;color:var(--blue);letter-spacing:1px;line-height:1}
.brand-dot{border-radius:50%;background:var(--sky);flex:none}
.brand-text{display:flex;flex-direction:column;gap:3px}
.brand-tag{font-size:12.5px;color:var(--sky);font-weight:400;line-height:1}
/* header */
.site-header{left:0;top:0;width:1200px;height:102px;background:var(--white)}
.site-header .brand{left:74px;top:28px;display:flex;align-items:center;gap:10px}
.site-header .brand-dot{width:52px;height:52px}
.site-header .brand-name{font-size:34px}
.main-nav a{position:absolute;top:46px;font-size:13px;color:#333;text-decoration:none;font-weight:500}
.btn{position:absolute;display:flex;align-items:center;gap:14px;background:var(--blue);color:var(--white);font-size:13px;font-weight:500;padding:0 14px;border-radius:3px;box-shadow:0 4px 10px rgba(31,104,164,.35);text-decoration:none;white-space:nowrap}
.btn svg{width:14px;height:14px;flex:none}
.nav-cta{left:1002px;top:32px;width:122px;height:41px;justify-content:center;text-transform:uppercase;font-size:13px;box-shadow:none}
/* hero */
.hero{left:0;top:102px;width:1200px;height:534px;background:linear-gradient(90deg,#d9d2cc 0%,#eef0f2 30%,#f3f5f7 55%,#ddd5cf 80%,#cfc5bd 100%)}
.hero .brand-dot{position:absolute;left:498px;top:100px;width:202px;height:202px;background:var(--blue)}
.hero .brand-name{position:absolute;left:0;width:1200px;top:328px;text-align:center;font-size:70px}
.hero .tagline{position:absolute;left:0;width:1200px;top:390px;text-align:center;font-size:24px;color:var(--sky);font-weight:300}
/* quotes */
.quote{left:0;width:1200px;text-align:center;color:var(--blue);text-transform:uppercase;font-size:23px;line-height:39px;letter-spacing:.5px}
.quote .mark{color:var(--sky);font-weight:600;font-size:30px;vertical-align:-4px}
.quote-author{left:0;width:1200px;text-align:center;color:var(--sky);font-size:16px}
/* sections */
.section-title{left:74px;font-size:34px;font-weight:400;color:var(--blue)}
.sub{font-size:18px;color:var(--sky);font-weight:400;line-height:27px}
.copy{font-size:12.4px;line-height:22.5px;color:var(--text)}
.photo{border-radius:3px;box-shadow:0 6px 18px rgba(0,0,0,.18)}
/* bio list */
.quals{left:521px;top:2796px;list-style:none;width:600px}
.quals li{position:relative;padding-left:28px;font-size:13.2px;line-height:22px;margin-bottom:23px;color:#555}
.quals li::before{content:"";position:absolute;left:2px;top:5px;width:13px;height:13px;border-radius:50%;background:var(--sky)}
/* contact */
.contact-band{left:0;top:3486px;width:1200px;height:398px;background:var(--blue-dark)}
.contact-card{left:73px;top:3373px;width:1051px;height:438px;background:var(--white);box-shadow:0 6px 22px rgba(0,0,0,.1)}
.field{position:absolute;border-bottom:1px solid var(--line);background:var(--field);font-size:11.5px;color:#777;padding:6px 6px}
/* footer */
.site-footer{left:0;top:3884px;width:1200px;height:99px;background:var(--white)}
.site-footer .brand{position:absolute;left:74px;top:26px;display:flex;align-items:center;gap:10px}
.site-footer .brand-dot{width:52px;height:52px}
.site-footer .brand-name{font-size:34px}
.site-footer a{position:absolute;top:42px;font-size:12.5px;color:#555;text-decoration:none}
</style>
</head>
<body>

<header class="site-header abs">
  <div class="brand abs"><span class="brand-dot"></span><span class="brand-text"><span class="brand-name">WALLBRECHT</span><span class="brand-tag">Training &amp; Coaching Rund um Geburt</span></span></div>
  <nav class="main-nav">
    <a style="left:567px">Für Eltern</a>
    <a style="left:685px">Für Geburtshilfe-Profis</a>
    <a style="left:884px">Über mich</a>
  </nav>
  <a class="btn nav-cta">Kontakt</a>
</header>

<section class="hero abs" role="img" aria-label="Hintergrundfotos: lächelnde Frau und Eltern mit Neugeborenem, hell überblendet">
  <span class="brand-dot"></span>
  <div class="brand-name">WALLBRECHT</div>
  <div class="tagline">Training &amp; Coaching Rund um Geburt</div>
</section>

<p class="quote abs" style="top:678px"><span class="mark">„</span> A woman, as long as she lives,<br>will remember how she was made to feel at her birth. <span class="mark">“</span></p>
<p class="quote-author abs" style="top:763px">Lena Marbach</p>

<!-- Für Eltern -->
<h2 class="section-title abs" style="top:860px">Für Eltern</h2>
<div class="photo abs" style="left:74px;top:925px;width:334px;height:420px;background:linear-gradient(160deg,#e9d6c6,#f1ece6 55%,#c9b8a8)" role="img" aria-label="Foto: schlafendes Neugeborenes in gemusterter Decke"></div>
<h3 class="sub abs" style="left:521px;top:933px">Geburt vorbereiten</h3>
<p class="copy abs" style="left:521px;top:974px;width:603px">Das Geburtsvorbereitungsprogramm für Dich und Deinen Partner. Für ein natürliches Erleben von Geburt. Das Geburtsvorbereitungsprogramm für Dich und Deinen Partner. Für ein natürliches Erleben von Geburt.</p>
<a class="btn" style="left:521px;top:1057px;width:334px;height:42px">Mehr zur Geburtvorbereitung erfahren <svg viewBox="0 0 14 14"><path d="M2 7h10M8 3l4 4-4 4" stroke="#fff" stroke-width="1.6" fill="none"/></svg></a>
<h3 class="sub abs" style="left:521px;top:1158px">Geburt aufarbeiten</h3>
<p class="copy abs" style="left:521px;top:1199px;width:603px">Du hattest eine schwierige Geburt mit Deinem Kind und die Erinnerung daran ist für Dich stressbeladen? Und dies steht Dir vielleicht im Wege für eine neue Schwangerschaft?</p>
<a class="btn" style="left:521px;top:1279px;width:334px;height:42px">Mehr zur Geburtaufarbeitung erfahren <svg viewBox="0 0 14 14"><path d="M2 7h10M8 3l4 4-4 4" stroke="#fff" stroke-width="1.6" fill="none"/></svg></a>

<!-- Für Geburtshilfeprofis -->
<h2 class="section-title abs" style="top:1448px">Für Geburtshilfeprofis</h2>
<h3 class="sub abs" style="left:74px;top:1533px">Selbstfürsorge für Hebammen und ÄrztInnen:<br>HebaCura mit PEK®</h3>
<div class="abs" style="left:74px;top:1609px;width:600px">
  <p class="copy">Die Erfahrungen und Erlebnisse bei Geburten sind nicht immer angenehm und manchmal auch ganz schön heftig. GeburtsbegleiterInnen nehmen öfters etwas “mit nach Hause”… Und nicht nur das, möglicherweise nehmen sie die schlimmen Erfahrungen in die nächste Geburt mit hinein, die sie begleiten. Vielleicht kommt ihnen mit der Zeit die Zuversicht und Leichtigkeit abhanden oder es fällt ihnen immer schwerer, der Kraft der natürlichen Geburt zu vertrauen.</p>
  <p class="copy" style="margin-top:22px">HebaCura mit PEK® bietet ein schnell zu erlernendes Selbsthilfe-Werkzeug, um sich emotional zu regulieren und dysfunktionale Gefühle zu integrieren und zu transformieren – ohne Verdrängung und ohne Retraumatisierung. Und auch Vorwürfe an sich selbst und andere lassen sich leicht auflösen.</p>
  <p class="copy" style="margin-top:22px">Mit PEK®, der Prozess- und Embodimentfokussierten Psychologie nach Dr. Martin Kessel, können Menschen in helfenden Berufen sich selbst schnell und selbstständig in emotional belastenden Situationen regulieren und dadurch auch sekundäre Traumatisierungen vermeiden.</p>
</div>
<a class="btn" style="left:74px;top:1995px;width:289px;height:42px">Ausschreibung herunterladen <svg viewBox="0 0 14 14"><path d="M7 2v10M3 8l4 4 4-4" stroke="#fff" stroke-width="1.6" fill="none"/></svg></a>
<div class="photo abs" style="left:788px;top:1538px;width:336px;height:382px;background:linear-gradient(150deg,#d8c9b9,#efe6c8 40%,#d9b8c8 75%,#bfa8b8)" role="img" aria-label="Foto: Hebamme berät eine Mutter mit Baby"></div>

<!-- Traumaprävention -->
<div class="photo abs" style="left:74px;top:2154px;width:337px;height:382px;background:linear-gradient(160deg,#e8e8ea,#d7c4c4 45%,#c9879a 70%,#8aa4c8)" role="img" aria-label="Foto: Hebamme untersucht eine schwangere Frau"></div>
<h3 class="sub abs" style="left:521px;top:2149px">TraumaPrävention in der Geburtshilfe</h3>
<div class="abs" style="left:521px;top:2193px;width:603px">
  <p class="copy">In der Geburtshilfe zu arbeiten – dazu haben sich Hebammen, Ärztinnen und Ärzte irgendwann einmal entschieden. Es war eine mutige Entscheidung – begegnen sie doch Tag für Tag sowohl dem Wunder als auch der Verletzlichkeit des Lebens. Sie tragen eine hohe Verantwortung bei der Begleitung eines natürlichen Prozesses, dessen Verlauf nicht vorhersehbar und ohne massive Eingriffe nur wenig steuerbar scheint.</p>
  <p class="copy" style="margin-top:22px">Bis zu dem allseits gewünschten Ausgang, dass Mutter und Kind wohlauf sind, kann so viel geschehen, was Auswirkungen haben kann, die weit über den kleinsten Nenner von „Das Kind ist da und wohl auf, egal wie“ hinausreichen.</p>
  <p class="copy" style="margin-top:22px">Wie weitreichend die Auswirkungen einer Traumatisierung der Mutter bei der Geburt sein können, wird immer offensichtlicher. Der Beginn der Familienbeziehung, die Stillbeziehung, die Selbstbeziehung – all das kann gestört sein, wenn eine Frau ihr Geburtserlebnis als belastend empfindet. Und natürlich ist eine schwierige Geburt auch für das Baby sehr belastend.</p>
</div>
<a class="btn" style="left:521px;top:2580px;width:289px;height:42px">Ausschreibung herunterladen <svg viewBox="0 0 14 14"><path d="M7 2v10M3 8l4 4 4-4" stroke="#fff" stroke-width="1.6" fill="none"/></svg></a>

<!-- Über mich -->
<h2 class="section-title abs" style="left:72px;top:2717px">Mira Solveig Wallbrecht – Die Geburtsverbesserin</h2>
<div class="photo abs" style="left:74px;top:2798px;width:334px;height:402px;background:radial-gradient(circle at 50% 45%,#c8a08a,#6e5346 60%,#3d3a44)" role="img" aria-label="Porträtfoto der Trainerin"></div>
<ul class="quals abs">
  <li>NLP Trainerin (DVKT)</li>
  <li>Systemischer MasterCoach (DVKT)</li>
  <li>SanftGeboren 2.0 Coach seit 2013 (www.sanftgeboren-suedwest.de)</li>
  <li>Co-Autorin von „Mama werden mit SanftGeboren“, Lindenhof-Verlag München 2016</li>
  <li>Gesundheitscoach</li>
  <li>Fortbildung Prozess- und Embodimentfokussierte - Psychologie PEK® (nach Dr. Kessel)</li>
  <li>Trauma Release Method Practitioner</li>
  <li>Hui Chun Gong Lehrerin</li>
  <li>Mutter eines erwachsenen Sohnes</li>
</ul>

<p class="quote abs" style="top:3277px;font-size:24px"><span class="mark">„</span> Jeder Mensch wird nur einmal geboren. <span class="mark">“</span></p>

<!-- Kontakt -->
<div class="contact-band abs"></div>
<section class="contact-card abs">
  <div class="photo abs" style="left:60px;top:61px;width:244px;height:318px;background:linear-gradient(160deg,#c9b8a6,#e8dccd 50%,#b59c86)" role="img" aria-label="Foto: Hand hält ein Smartphone mit Kommunikationssymbolen"></div>
  <h3 class="sub abs" style="left:357px;top:54px">Ich berate Sie gerne</h3>
  <p class="abs" style="left:357px;top:122px;font-size:12px;font-weight:600;color:var(--blue)">01234 567890</p>
  <p class="abs" style="left:357px;top:153px;font-size:12px;font-weight:600;color:var(--blue)">info@wallbrecht-geburt.de</p>
  <p class="abs" style="left:357px;top:209px;font-size:11.5px;line-height:29px;color:#555">Mira Solveig Wallbrecht –<br>Die Geburtsverbesserin<br>Musterstraße 1<br>12345 Musterhausen</p>
  <h3 class="sub abs" style="left:627px;top:54px">Jetzt Kontakt aufnehmen</h3>
  <div class="field" style="left:627px;top:103px;width:170px;height:29px">Name *</div>
  <div class="field" style="left:811px;top:103px;width:172px;height:29px">Vorname</div>
  <div class="field" style="left:627px;top:149px;width:170px;height:29px">Telefonnummer</div>
  <div class="field" style="left:811px;top:149px;width:172px;height:29px">E-Mail *</div>
  <div class="field" style="left:627px;top:198px;width:356px;height:113px;padding-top:10px">Nachricht *</div>
  <a class="btn" style="left:627px;top:334px;width:133px;height:42px">Absenden <svg viewBox="0 0 14 14"><path d="M2 7h10M8 3l4 4-4 4" stroke="#fff" stroke-width="1.6" fill="none"/></svg></a>
</section>

<footer class="site-footer abs">
  <div class="brand"><span class="brand-dot"></span><span class="brand-text"><span class="brand-name">WALLBRECHT</span><span class="brand-tag">Training &amp; Coaching Rund um Geburt</span></span></div>
  <a style="left:892px">Impressum</a>
  <a style="left:986px">Datenschutzerklärung</a>
</footer>

</body>
</html>
```